Business cards to launch an education platform

Hi,
I am looking at having new business cards designed.
I am a startup, developing a web platform for schools and university, the education world. It's an online assessment system.
I would like a card that looks classy, and that is using the colors and the font of my logo.

I have attached:
1) my logo
2) A business card that I have designed quickly so you can have all the information required in the card, but I really don't like it.
3) The font that I am using (Lato Regular) to design my web platform
4) Some screenshots of my web platform so you can have a look at the style that I have.

Target Market(s)

Major market: Education system: Schools and university
Minor markets: Business in general

Industry/Entity Type

Business

Contact Information for Business Card

Lydia Marsh
Director

M: 0437 681 902
E: lydia.marsh@copperLeafSystems.com.au

Requirements
Must have
• The colors of my logo

```html
<!DOCTYPE html>
<html lang="en">
<head>
<meta charset="utf-8">
<title>Copper Leaf Systems — Business Card</title>
<link rel="stylesheet" href="https://fonts.googleapis.com/css2?family=Lato:wght@300;400&display=swap">
<style>
  :root {
    --backdrop: #ddd7d0;
    --card: #ffffff;
    --brand-blue: #1f4f8c;
    --text-grey: #8c8c8c;
    --rule-grey: #b9b9b9;
    --card-shadow: rgba(60, 50, 40, 0.18);
  }
  * { margin: 0; padding: 0; box-sizing: border-box; }
  html, body {
    width: 1200px;
    height: 884px;
    overflow: hidden;
    background: var(--backdrop);
    font-family: "Lato", sans-serif;
  }
  .canvas {
    position: relative;
    width: 1200px;
    height: 884px;
  }
  .card {
    position: absolute;
    left: 300px;
    width: 600px;
    height: 343px;
    background: var(--card);
    box-shadow: 0 10px 30px var(--card-shadow);
  }
  .card--front { top: 70px; }
  .card--back { top: 471px; }

  .brand {
    position: absolute;
    left: 150px;
    top: 128px;
    width: 330px;
  }
  .brand__rule {
    border-top: 1px dotted var(--rule-grey);
    margin-bottom: 22px;
  }
  .brand__lockup {
    display: flex;
    align-items: center;
    gap: 16px;
  }
  .brand__square {
    width: 58px;
    height: 58px;
    background: var(--brand-blue);
    flex: none;
  }
  .brand__name {
    color: var(--brand-blue);
    font-weight: 400;
    font-size: 30px;
    line-height: 1.05;
    letter-spacing: 1px;
  }

  .person {
    position: absolute;
    left: 90px;
    top: 62px;
  }
  .person__name {
    color: var(--brand-blue);
    font-weight: 400;
    font-size: 24px;
    letter-spacing: 0.5px;
    line-height: 1.2;
  }
  .person__title {
    color: var(--text-grey);
    font-weight: 300;
    font-size: 16px;
    letter-spacing: 1px;
    margin-top: 4px;
  }

  .contact {
    position: absolute;
    left: 90px;
    top: 160px;
    color: var(--text-grey);
    font-weight: 300;
    font-size: 18px;
    line-height: 1.7;
    letter-spacing: 0.3px;
  }
  .contact__line--small { font-size: 15px; }
</style>
</head>
<body>
  <main class="canvas">
    <section class="card card--front" aria-label="Card front">
      <div class="brand">
        <div class="brand__rule"></div>
        <div class="brand__lockup">
          <span class="brand__square" aria-hidden="true"></span>
          <p class="brand__name">COPPER LEAF<br>Systems</p>
        </div>
      </div>
    </section>

    <section class="card card--back" aria-label="Card back">
      <div class="person">
        <p class="person__name">Lydia Marsh</p>
        <p class="person__title">Director</p>
      </div>
      <div class="contact">
        <p class="contact__line">M: 0437 681 902</p>
        <p class="contact__line">E: lydia.marsh@copperLeafSystems.com.au</p>
        <p class="contact__line">www.copperLeafSystems.com.au</p>
        <p class="contact__line contact__line--small">42 Harbour Lane, Level 3, West Wing</p>
      </div>
    </section>
  </main>
</body>
</html>
```